CFO services graphic design

I own a business consulting firm called Marlowe Consulting and we need a graphic for CFO services in our colours and branding. The attached file "CFO services to be put into Marlowe consulting theme", shows the content for the design. The two other files show the theme and colours for the new design.

```html
<!DOCTYPE html>
<html lang="en">
<head>
<meta charset="utf-8">
<title>Chief Financial Officer Services</title>
<link rel="stylesheet" href="https://fonts.googleapis.com/css2?family=Roboto:ital,wght@0,400;0,700;1,400&display=swap">
<style>
  :root {
    --navy: #1b2550;
    --blue: #2eb0e4;
    --orange: #f39325;
    --halo: #e6e6e6;
    --white: #ffffff;
    --icon-tint: #d3eef9;
  }
  html, body {
    margin: 0;
    padding: 0;
    width: 1200px;
    height: 1200px;
    overflow: hidden;
    background: var(--white);
  }
  .cfo-wheel { display: block; width: 1200px; height: 1200px; }
  .petal-halo { fill: var(--halo); }
  .petal-face { fill: var(--white); }
  .ring-base { fill: none; stroke: var(--blue); stroke-width: 11; }
  .ring-accent { fill: none; stroke: var(--orange); stroke-width: 11; stroke-dasharray: 530 425; }
  .hub-halo { fill: var(--halo); }
  .hub-gap { fill: var(--white); }
  .hub-core { fill: var(--navy); }
  .icon-slot { fill: var(--icon-tint); }
  .label {
    font-family: "Roboto", sans-serif;
    font-weight: 700;
    font-size: 21px;
    fill: var(--navy);
    text-anchor: middle;
  }
  .label-note {
    font-family: "Roboto", sans-serif;
    font-style: italic;
    font-weight: 400;
    font-size: 17px;
    fill: var(--navy);
    text-anchor: middle;
  }
  .hub-title {
    font-family: "Roboto", sans-serif;
    font-weight: 700;
    font-size: 44px;
    fill: var(--white);
    text-anchor: middle;
  }
</style>
</head>
<body>
<svg class="cfo-wheel" viewBox="0 0 1200 1200" xmlns="http://www.w3.org/2000/svg">

  <!-- petals -->
  <g class="petal" transform="translate(349 349)">
    <circle class="petal-halo" r="185"/><circle class="petal-face" r="170"/>
    <circle class="ring-base" r="152"/><circle class="ring-accent" r="152" transform="rotate(-110)"/>
  </g>
  <g class="petal" transform="translate(349 851)">
    <circle class="petal-halo" r="185"/><circle class="petal-face" r="170"/>
    <circle class="ring-base" r="152"/><circle class="ring-accent" r="152" transform="rotate(130)"/>
  </g>
  <g class="petal" transform="translate(245 600)">
    <circle class="petal-halo" r="185"/><circle class="petal-face" r="170"/>
    <circle class="ring-base" r="152"/><circle class="ring-accent" r="152" transform="rotate(-165)"/>
  </g>
  <g class="petal" transform="translate(600 955)">
    <circle class="petal-halo" r="185"/><circle class="petal-face" r="170"/>
    <circle class="ring-base" r="152"/><circle class="ring-accent" r="152" transform="rotate(100)"/>
  </g>
  <g class="petal" transform="translate(851 851)">
    <circle class="petal-halo" r="185"/><circle class="petal-face" r="170"/>
    <circle class="ring-base" r="152"/><circle class="ring-accent" r="152" transform="rotate(60)"/>
  </g>
  <g class="petal" transform="translate(955 600)">
    <circle class="petal-halo" r="185"/><circle class="petal-face" r="170"/>
    <circle class="ring-base" r="152"/><circle class="ring-accent" r="152" transform="rotate(15)"/>
  </g>
  <g class="petal" transform="translate(851 349)">
    <circle class="petal-halo" r="185"/><circle class="petal-face" r="170"/>
    <circle class="ring-base" r="152"/><circle class="ring-accent" r="152" transform="rotate(-20)"/>
  </g>
  <g class="petal" transform="translate(600 245)">
    <circle class="petal-halo" r="185"/><circle class="petal-face" r="170"/>
    <circle class="ring-base" r="152"/><circle class="ring-accent" r="152" transform="rotate(-75)"/>
  </g>

  <!-- hub -->
  <g class="hub" transform="translate(600 600)">
    <g class="hub-spikes">
      <polygon class="hub-halo" points="-28,-230 0,-290 28,-230" transform="rotate(0)"/>
      <polygon class="hub-halo" points="-28,-230 0,-290 28,-230" transform="rotate(45)"/>
      <polygon class="hub-halo" points="-28,-230 0,-290 28,-230" transform="rotate(90)"/>
      <polygon class="hub-halo" points="-28,-230 0,-290 28,-230" transform="rotate(135)"/>
      <polygon class="hub-halo" points="-28,-230 0,-290 28,-230" transform="rotate(180)"/>
      <polygon class="hub-halo" points="-28,-230 0,-290 28,-230" transform="rotate(225)"/>
      <polygon class="hub-halo" points="-28,-230 0,-290 28,-230" transform="rotate(270)"/>
      <polygon class="hub-halo" points="-28,-230 0,-290 28,-230" transform="rotate(315)"/>
    </g>
    <circle class="hub-halo" r="245"/>
    <circle class="hub-gap" r="219"/>
    <circle class="hub-core" r="209"/>
    <text class="hub-title" y="563" transform="translate(0 -600)">CHIEF</text>
    <text class="hub-title" y="615" transform="translate(0 -600)">FINANCIAL</text>
    <text class="hub-title" y="667" transform="translate(0 -600)">OFFICER</text>
  </g>

  <!-- icons -->
  <rect class="icon-slot" x="586" y="150" width="58" height="58" rx="8" role="img" aria-label="Icon: money bag with calculator"/>
  <rect class="icon-slot" x="845" y="252" width="74" height="66" rx="8" role="img" aria-label="Icon: money bag and house on a tray"/>
  <rect class="icon-slot" x="948" y="525" width="66" height="58" rx="8" role="img" aria-label="Icon: target with arrow"/>
  <rect class="icon-slot" x="822" y="815" width="66" height="70" rx="8" role="img" aria-label="Icon: monitor with report and chart"/>
  <rect class="icon-slot" x="568" y="910" width="64" height="62" rx="8" role="img" aria-label="Icon: financial report scroll with bar chart"/>
  <rect class="icon-slot" x="293" y="773" width="70" height="70" rx="8" role="img" aria-label="Icon: open ledger with calculator and pen"/>
  <rect class="icon-slot" x="190" y="506" width="74" height="70" rx="8" role="img" aria-label="Icon: bank building with columns"/>
  <rect class="icon-slot" x="313" y="220" width="70" height="76" rx="8" role="img" aria-label="Icon: organisation chart of people"/>

  <!-- labels -->
  <text class="label" x="620" y="239">Cost Accounting</text>
  <text class="label" x="620" y="264">&amp; Cost</text>
  <text class="label" x="620" y="290">Management</text>

  <text class="label" x="882" y="349">Capital</text>
  <text class="label" x="882" y="374">Structure &amp;</text>
  <text class="label" x="882" y="400">the Cost of</text>
  <text class="label" x="882" y="426">Capital</text>

  <text class="label" x="980" y="617">Long-term &amp;</text>
  <text class="label" x="980" y="643">short-term</text>
  <text class="label" x="980" y="668">investment</text>
  <text class="label" x="980" y="694">decisions</text>

  <text class="label" x="855" y="918">Performance</text>
  <text class="label" x="855" y="944">Evaluation</text>

  <text class="label" x="600" y="1003">Budgeting &amp;</text>
  <text class="label" x="600" y="1029">Strategic</text>
  <text class="label" x="600" y="1055">Planning</text>

  <text class="label" x="327" y="877">Risk</text>
  <text class="label" x="327" y="903">Management</text>

  <text class="label" x="225" y="607">Compliance:</text>
  <text class="label-note" x="225" y="632">tax, legal &amp; regulatory</text>

  <text class="label" x="348" y="322">Communication:</text>
  <text class="label-note" x="348" y="342">Board of Directors, creditors,</text>
  <text class="label-note" x="348" y="364">owners, investors, credit</text>
  <text class="label-note" x="348" y="385">rating agencies</text>
</svg>
</body>
</html>
```